Bref créative
Quorvant Systems
Professional
Ramesh Tolanimurthy
Chief Executive Officer
27 Sec. 61, Kusum Marg
Bhavanipur, Jaipur
RJ 304417 INDIA
ramesh@quorvant.example
www.quorvant.example
Need business cards and stationery. I am open to design ideas and feedback will be provided timely
Our email address for letterhead/fax is contact@quorvant.example. This should be used in all locations except the business card.
Stationary and envelopes with a watermark would look great !
Use Horizontal Logo provided in files.
www.quorvant.example can also be added few lines below the logo

```html
<!DOCTYPE html>
<html lang="en">
<head>
<meta charset="utf-8">
<title>Quorvant Systems – Business Cards</title>
<link rel="stylesheet" href="https://fonts.googleapis.com/css2?family=Source+Sans+3:ital,wght@0,400;0,600;0,700;1,700&display=swap">
<style>
  :root {
    --bg: #ececec;
    --card: #ffffff;
    --blue-dark: #1479c4;
    --blue-light: #3fa9e8;
    --grey: #a9abae;
    --ink-white: #ffffff;
    --brand: #1a86d0;
  }
  * { box-sizing: border-box; margin: 0; padding: 0; }
  html, body { width: 1200px; height: 852px; overflow: hidden; }
  body {
    background: var(--bg);
    font-family: "Source Sans 3", "PT Sans", sans-serif;
    position: relative;
  }
  .card {
    position: absolute;
    width: 540px;
    height: 310px;
    background: var(--card);
    border-radius: 22px;
    overflow: hidden;
    box-shadow: 0 6px 18px rgba(0,0,0,0.18);
  }
  .card--left  { left: 60px;  top: 90px; }
  .card--right { left: 600px; top: 452px; }
  .card__art { position: absolute; inset: 0; width: 100%; height: 100%; }
  .holder { position: absolute; color: var(--ink-white); }
  .holder__name { font-weight: 700; font-style: italic; font-size: 19px; line-height: 1.1; }
  .holder__role { font-size: 13px; margin-top: 2px; }
  .address { position: absolute; color: var(--ink-white); font-size: 12.5px; line-height: 1.35; }
  .contacts { position: absolute; list-style: none; color: var(--ink-white); font-size: 12.5px; line-height: 1.55; }
  .contacts li { display: flex; align-items: center; gap: 8px; }
  .contacts svg { width: 13px; height: 13px; flex: none; }
  .brand { position: absolute; display: flex; align-items: center; gap: 10px; white-space: nowrap; }
  .brand__mark { width: 38px; height: 38px; border-radius: 50%; background: var(--brand); flex: none; }
  .brand__name {
    font-weight: 700; font-size: 24px; letter-spacing: 1px; line-height: 0.95;
    color: var(--brand); text-transform: uppercase;
  }
  .brand__name span { display: block; font-size: 12px; letter-spacing: 3.5px; margin-top: 2px; }
  .card--right .holder, .card--right .address { text-align: right; }
  .card--right .contacts li { justify-content: flex-end; }
</style>
</head>
<body>

<svg width="0" height="0" style="position:absolute" aria-hidden="true">
  <defs>
    <linearGradient id="bandBlue" x1="0" y1="0" x2="1" y2="1">
      <stop offset="0" stop-color="#3fa9e8"/>
      <stop offset="1" stop-color="#1479c4"/>
    </linearGradient>
    <symbol id="i-phone" viewBox="0 0 16 16"><path fill="#fff" d="M4 1l3 3-2 2c1 2 3 4 5 5l2-2 3 3-2 3C7 15 1 9 1 3z"/></symbol>
    <symbol id="i-mobile" viewBox="0 0 16 16"><rect x="4" y="1" width="8" height="14" rx="1.5" fill="#fff"/><rect x="5.5" y="3" width="5" height="8" fill="#1e8ad4"/></symbol>
    <symbol id="i-fax" viewBox="0 0 16 16"><rect x="1" y="6" width="14" height="7" rx="1" fill="#fff"/><rect x="4" y="2" width="8" height="5" fill="#fff"/></symbol>
    <symbol id="i-mail" viewBox="0 0 16 16"><circle cx="8" cy="8" r="7" fill="#fff"/><path d="M4 6h8v5H4z M4 6l4 3 4-3" fill="none" stroke="#1e8ad4" stroke-width="1"/></symbol>
    <symbol id="i-web" viewBox="0 0 16 16"><circle cx="8" cy="8" r="7" fill="#fff"/><path d="M1 8h14M8 1c-3 4-3 10 0 14M8 1c3 4 3 10 0 14" fill="none" stroke="#1e8ad4" stroke-width="1"/></symbol>
  </defs>
</svg>

<article class="card card--left">
  <svg class="card__art" viewBox="0 0 540 310" aria-hidden="true">
    <path d="M232 0 H268 C318 120 400 240 540 258 V276 C380 256 300 125 250 0 Z" fill="var(--grey)"/>
    <path d="M0 0 H250 C300 125 380 256 540 276 V310 H0 Z" fill="url(#bandBlue)"/>
  </svg>
  <div class="holder" style="left:22px; top:26px;">
    <p class="holder__name">Ramesh Tolanimurthy</p>
    <p class="holder__role">Chief Executive Officer</p>
  </div>
  <p class="address" style="left:22px; top:118px;">27 Sec. 61, Kusum Marg<br>Bhavanipur, Jaipur<br>RJ 304417 INDIA</p>
  <ul class="contacts" style="left:22px; top:178px;">
    <li><svg><use href="#i-phone"/></svg>91 141 5550147</li>
    <li><svg><use href="#i-mobile"/></svg>91 9000012345</li>
    <li><svg><use href="#i-fax"/></svg>91 141 5550147</li>
    <li><svg><use href="#i-mail"/></svg>ramesh@quorvant.example</li>
    <li><svg><use href="#i-web"/></svg>www.quorvant.example</li>
  </ul>
  <div class="brand" style="left:318px; top:66px;">
    <div class="brand__mark"></div>
    <p class="brand__name">Quorvant<span>Systems</span></p>
  </div>
</article>

<article class="card card--right">
  <svg class="card__art" viewBox="0 0 540 310" aria-hidden="true">
    <path d="M308 0 H272 C222 120 140 240 0 258 V276 C160 256 240 125 290 0 Z" fill="var(--grey)"/>
    <path d="M540 0 H290 C240 125 160 256 0 276 V310 H540 Z" fill="url(#bandBlue)"/>
  </svg>
  <div class="holder" style="right:22px; top:26px;">
    <p class="holder__name">Ramesh Tolanimurthy</p>
    <p class="holder__role">Chief Executive Officer</p>
  </div>
  <p class="address" style="right:22px; top:100px;">27 Sec. 61, Kusum Marg<br>Bhavanipur, Jaipur<br>RJ 304417 INDIA</p>
  <ul class="contacts" style="right:22px; top:168px;">
    <li>91 141 5550147<svg><use href="#i-phone"/></svg></li>
    <li>91 9000012345<svg><use href="#i-mobile"/></svg></li>
    <li>91 141 5550147<svg><use href="#i-fax"/></svg></li>
    <li>ramesh@quorvant.example<svg><use href="#i-mail"/></svg></li>
    <li>www.quorvant.example<svg><use href="#i-web"/></svg></li>
  </ul>
  <div class="brand" style="left:18px; top:76px;">
    <div class="brand__mark"></div>
    <p class="brand__name">Quorvant<span>Systems</span></p>
  </div>
</article>

</body>
</html>
```